Law Firm
To All Designers:
New e-mail address for the project is daniel@rvestlegal.net.
Thanks. I love all the designs.
P.S. I like the orange on the one side of the card as opposed to black.
@ph - New drafts #161 & #162 in lieu of 145 & 146 are submitted, Can you please check & provide feedback in private message.
Thanks
draft #145 and #146 Drafts came out black and I cannot see them (look like negatives). Please resubmit. Thanks.
Please DO NOT PUT "Gavels", "Scales of Justice" "Court Buildings", etc. on the card. I DO NOT WANT IT.
Thanks.
draft #130 Card looks a lot better. Can I see it with the dot at the end of the big line through the card a little smaller (but that is the look I was going for) and can I see some color (black, orange and/or grey) below that line where the address, phone and e-mail appear? Also, can I see with just the "m" and the line part of the logo on the other side? Thanks.
draft #125 and #126 Looks better. I didn't like the "watermark" "m" in my logo being sideways on the card (it didn't look like an "m" anymore to me that way), but Ido like it on the stationary and envelope. Can I see the card with the same orange on the one side with the orange line under the "m" in my logo at the bottom of the card then the address, telephone and e-mail below it? Thanks.
To all designers,
Can I start seeing letterhead, envelopes, fax covers and e-mail signatures too! I look forward to seeing the designs!
draft #49 I like the line under my name like in the logo. Can I see with orange on the other side of the card?
drafts #101, #102, #103 and #104 I would like to see with orange on the other side of the card rather than black
I like the use of the whites and oranges with black accents. So not too much black. I also like orange with the logo (either with the text or just the script "m") on one side of the card. Thanks for all the great designs.
draft #35 I like the use of the logo at the bottom of the card. But "no "scales of justice", "court buildings" or "gavels", etc. was not something I wanted on the card, it was just an instruction to the designers that although I am a lawyer, I do not want to use these symbols.
draft #31 and #32 Maybe you could use the orange line under the script "m" under the logo for the "white space"?
draft #31 and #32 Like the use of the colors in the card and the "watermark" logo on the stationary. However, there is too much "white space" on the right side of the card. Other drafts did better job with "white space". I would also like to maybe see the "watermark" logo used in the card as well.

```html
<!DOCTYPE html>
<html lang="en">
<head>
<meta charset="utf-8">
<title>Daniel R. Vest, P.C. — Business Card</title>
<link rel="stylesheet" href="https://fonts.googleapis.com/css2?family=Libre+Baskerville:wght@400;700&display=swap">
<style>
  :root {
    --backdrop: #cfcfcf;
    --card-white: #fbfbfb;
    --card-dark: #3a3a3c;
    --card-orange: #e0642a;
    --ink: #2b2b2d;
    --ink-soft: #5a5a5c;
    --accent: #e0642a;
    --paper-text: #ffffff;
  }
  * { margin: 0; padding: 0; box-sizing: border-box; }
  html, body { width: 1200px; height: 799px; overflow: hidden; }
  body {
    background: var(--backdrop);
    font-family: "Libre Baskerville", Georgia, serif;
    position: relative;
  }
  .card {
    position: absolute;
    width: 525px;
    height: 300px;
    box-shadow: 0 6px 18px rgba(0,0,0,0.18);
  }
  .card--back {
    left: 70px;
    top: 90px;
    background: var(--card-orange);
    display: flex;
    flex-direction: column;
    align-items: center;
    justify-content: center;
    color: var(--paper-text);
  }
  .card--front {
    left: 605px;
    top: 409px;
    background: var(--card-white);
    overflow: hidden;
  }
  .firm-name {
    font-weight: 700;
    text-transform: uppercase;
    letter-spacing: 0.04em;
    font-size: 27px;
    line-height: 1;
    white-space: nowrap;
  }
  .firm-tagline {
    font-weight: 700;
    text-transform: uppercase;
    letter-spacing: 0.18em;
    font-size: 11px;
    margin-top: 10px;
    white-space: nowrap;
  }
  .card--back .firm-tagline { border-top: 1px solid var(--paper-text); padding-top: 7px; }
  .front-logo {
    position: absolute;
    left: 32px;
    top: 112px;
    width: 260px;
    color: var(--ink);
  }
  .front-logo .firm-name { font-size: 18px; letter-spacing: 0.02em; }
  .front-logo .firm-tagline { font-size: 8.5px; letter-spacing: 0.16em; border-top: 1px solid var(--ink); padding-top: 6px; margin-top: 8px; width: 190px; }
  .person {
    position: absolute;
    left: 330px;
    top: 88px;
  }
  .person-name {
    color: var(--accent);
    font-weight: 700;
    font-size: 16px;
    white-space: nowrap;
  }
  .person-role {
    color: var(--ink-soft);
    font-size: 11px;
    margin-top: 4px;
  }
  .contact-list {
    position: absolute;
    left: 330px;
    top: 176px;
    list-style: none;
    font-size: 11px;
    color: var(--ink);
  }
  .contact-list li { display: flex; align-items: center; gap: 8px; margin-bottom: 6px; white-space: nowrap; }
  .icon { width: 12px; height: 12px; flex: none; }
  .address {
    position: absolute;
    left: 32px;
    top: 214px;
    display: flex;
    gap: 8px;
    font-size: 11px;
    line-height: 1.5;
    color: var(--ink);
  }
  .address .icon { margin-top: 2px; }
  .base-band {
    position: absolute;
    left: 0;
    bottom: 0;
    width: 100%;
    height: 26px;
    background: var(--card-dark);
  }
  .accent-rule {
    position: absolute;
    left: 330px;
    bottom: 40px;
    width: 168px;
    height: 2px;
    background: var(--accent);
  }
</style>
</head>
<body>
  <section class="card card--back" aria-label="Card back">
    <div class="firm-name">Daniel R. Vest, P.C.</div>
    <div class="firm-tagline">Legal Consulting</div>
  </section>

  <section class="card card--front" aria-label="Card front">
    <div class="front-logo">
      <div class="firm-name">Daniel R. Vest, P.C.</div>
      <div class="firm-tagline">Legal Consulting</div>
    </div>

    <div class="person">
      <div class="person-name">Daniel R. Vest</div>
      <div class="person-role">Principal</div>
    </div>

    <ul class="contact-list">
      <li>
        <svg class="icon" viewBox="0 0 12 12" aria-hidden="true"><path d="M3 1 L5 3.5 L4 5 Q5 7 7 8 L8.5 7 L11 9 L9.5 11 Q5 11 1 6 Q1 3 3 1 Z" fill="var(--accent)"/></svg>
        (555) 014-2387
      </li>
      <li>
        <svg class="icon" viewBox="0 0 12 12" aria-hidden="true"><rect x="1" y="2.5" width="10" height="7" fill="var(--accent)"/><path d="M1 2.5 L6 7 L11 2.5" stroke="#fff" stroke-width="1" fill="none"/></svg>
        daniel@rvestlegal.net
      </li>
    </ul>

    <div class="address">
      <svg class="icon" viewBox="0 0 12 12" aria-hidden="true"><path d="M6 1 L11 6 H9.5 V11 H2.5 V6 H1 Z" fill="none" stroke="var(--accent)" stroke-width="1.3"/></svg>
      <div>27 Linden Road, Hartwell,<br>NY 10590</div>
    </div>

    <div class="accent-rule"></div>
    <div class="base-band"></div>
  </section>
</body>
</html>
```